Web Design - Personal Item Tags Portal

web page designs need to be created for a new company that provides item tracking tags and lets users register and report stolen/found items.
The theme of the designs needs to be energetic and convey a sense of freedom and adventure - where the user does not have to worry about their items since they have all been "tagged".
the client likes parts of the site at: http://www.brisklayouts.example/
they like:
1. slider images at top of pages. large slider on front page. fixed smaller height picture on internal pages
2. fixed company message on left-hand-side
3. My Account button to be clear and stand out

other comments:
clean, simple
• brand focused
• will have clear call to actions
• will include a description of what and why
• will appeal to both males and females

sections that the website will have are:
Home
About Us
How it works
Why
Case Studies
Uses and Applications
Shop
Contact Us

please create 2 designs : 1 home page, 1 internal page

Final winner will also require HTML slicing to be done.
Updates

hi, i have now updated the images so they work. sorry!

Hi, looking at all the designs that are coming in, alot of them are great. Designers need to remember to make the register for an account button more prominent. Also, there should be a "report found" and "report lost" buttons on the front-page and should be prominent as well.

Thanks

Hi, the customer has come back with a few comments and modifications for the designs, if you are able to make some tweaks to your submissions, that will be great:

The client would like the designs to be modified to highlight 3 main actions:
1. Log In/Register
2. Find an Owner
3. Lost an Item

The home page shouldnt be too content heavy in terms of text, it should only have major highlight points of what the system does (the 3 points listed above). the inner page designs are OK to have more text though.

i will also upload some notes from the customer that can be used as a guide and also include the design styles which the customer likes (but is not entirely happy with).

uploaded image files (3) with customer feedback comments

Industry/Entity Type

It Company

```html
<!DOCTYPE html>
<html lang="en">
<head>
<meta charset="utf-8">
<title>Wandertag — Home</title>
<link rel="stylesheet" href="https://fonts.googleapis.com/css2?family=Roboto+Condensed:wght@400;700&family=Mulish:wght@400&display=swap">
<style>
  :root {
    --ink: #000000;
    --paper: #ffffff;
    --accent: #3fb3d9;
    --nav-muted: #8a8a8a;
    --sub-grey: #8c8c8c;
    --body-text: #444444;
    --foot-text: #6a6a6a;
    --rule: #d4d4d4;
    --icon: #3a3a3a;
    --shadow: #7a7a7a;
  }
  * { box-sizing: border-box; margin: 0; padding: 0; }
  html, body { width: 1200px; height: 866px; overflow: hidden; background: var(--paper); }
  body { position: relative; font-family: "Mulish", sans-serif; }

  .site-header { position: absolute; left: 0; top: 0; width: 1200px; height: 38px; background: var(--ink); z-index: 3; }
  .main-nav { position: absolute; left: 213px; top: 0; height: 38px; display: flex; align-items: center; }
  .main-nav a {
    font-family: "Roboto Condensed", sans-serif; font-size: 15px; color: var(--nav-muted);
    text-decoration: none; padding: 0 12px; border-left: 1px dotted #555; line-height: 14px; letter-spacing: -0.2px;
  }
  .main-nav a:first-child { padding-left: 0; border-left: none; }
  .main-nav a.is-current { color: var(--paper); font-weight: 700; }
  .account-button {
    position: absolute; left: 890px; top: 0; width: 112px; height: 48px; background: var(--paper);
    border-bottom: 3px solid #c8c8c8; font-family: "Roboto Condensed", sans-serif; font-weight: 700;
    font-size: 16px; letter-spacing: -0.6px; color: var(--ink); text-decoration: none;
    display: flex; align-items: center; justify-content: center; padding-top: 4px;
  }

  .hero { position: absolute; left: 0; top: 38px; width: 1200px; height: 636px; background: var(--ink); overflow: hidden; }
  .hero-photo {
    position: absolute; left: 720px; top: 0; width: 480px; height: 636px;
    background: linear-gradient(180deg, #3a55c8 0%, #6f86d8 38%, #c9a2a0 62%, #f0a040 76%, #4b4f6a 88%, #1b2238 100%);
  }
  .hero-photo::before {
    content: ""; position: absolute; inset: 0;
    background: linear-gradient(100deg, #000 0%, #000 14%, rgba(0,0,0,0.85) 30%, rgba(0,0,0,0) 52%);
  }
  .brand-name {
    position: absolute; left: 213px; top: 178px; font-family: "Roboto Condensed", sans-serif;
    font-weight: 700; font-size: 64px; color: var(--paper); letter-spacing: -1px; line-height: 1;
  }
  .brand-tagline {
    position: absolute; left: 220px; top: 242px; font-family: "Roboto Condensed", sans-serif;
    font-size: 28px; color: var(--paper);
  }
  .company-name {
    position: absolute; left: 213px; top: 370px; font-family: "Roboto Condensed", sans-serif;
    font-size: 38px; color: var(--accent); letter-spacing: -0.8px; line-height: 1;
  }
  .company-offer {
    position: absolute; left: 286px; top: 408px; font-family: "Roboto Condensed", sans-serif;
    font-size: 19px; color: var(--sub-grey); letter-spacing: -0.2px; line-height: 1;
  }
  .register-button {
    position: absolute; left: 218px; top: 450px; width: 318px; height: 60px; background: var(--paper);
    box-shadow: 4px 4px 0 var(--shadow); font-family: "Roboto Condensed", sans-serif; font-weight: 700;
    font-size: 42px; letter-spacing: -1.6px; color: var(--ink); text-decoration: none;
    display: flex; align-items: center; justify-content: center;
  }

  .intro { position: absolute; left: 0; top: 674px; width: 1200px; height: 115px; border-bottom: 1px dotted var(--rule); }
  .intro-title {
    position: absolute; left: 213px; top: 32px; font-family: "Roboto Condensed", sans-serif;
    font-weight: 700; font-size: 31px; color: var(--accent); letter-spacing: -1px; line-height: 1;
  }
  .intro-title .amp { font-weight: 400; }
  .intro-divider { position: absolute; left: 411px; top: 38px; height: 22px; border-left: 1px dotted #999; }
  .intro-text {
    position: absolute; left: 426px; top: 34px; width: 574px; font-size: 11.6px; line-height: 14.4px; color: var(--body-text);
  }
  .intro-text a { color: var(--accent); text-decoration: none; }

  .site-footer { position: absolute; left: 0; top: 790px; width: 1200px; height: 76px; }
  .footer-links { position: absolute; left: 213px; top: 21px; font-size: 11px; color: var(--foot-text); }
  .footer-links a { color: var(--foot-text); text-decoration: none; }
  .footer-links .sep { margin: 0 7px; }
  .copyright { position: absolute; left: 213px; top: 37px; font-size: 11px; color: #9a9a9a; }
  .social-list { position: absolute; left: 633px; top: 30px; display: flex; gap: 5px; list-style: none; }
  .social-list li { width: 13px; height: 13px; border-radius: 3px; background: var(--icon); }
  .footer-brand {
    position: absolute; right: 202px; top: 26px; font-family: "Roboto Condensed", sans-serif;
    font-size: 16px; color: #9a9a9a;
  }
</style>
</head>
<body>
  <header class="site-header">
    <nav class="main-nav">
      <a class="is-current" href="#">Home</a>
      <a href="#">About Us</a>
      <a href="#">How It Works</a>
      <a href="#">Why</a>
      <a href="#">Case Studies</a>
      <a href="#">Uses and Applications</a>
      <a href="#">Shop</a>
      <a href="#">Contact Us</a>
    </nav>
    <a class="account-button" href="#">MY ACCOUNT</a>
  </header>

  <section class="hero">
    <div class="hero-photo" role="img" aria-label="Silhouette of a climber on a rock face against a blue and orange sunset sky over distant mountains"></div>
    <div class="brand-name">Wandertag</div>
    <p class="brand-tagline">. . . adventure first</p>
    <h1 class="company-name">Daring TAG Solutions</h1>
    <p class="company-offer">PROVIDES ITEM TRACKING TAGS</p>
    <a class="register-button" href="#">REGISTER NOW!</a>
  </section>

  <section class="intro">
    <h2 class="intro-title">WHAT <span class="amp">&amp;</span> WHY?</h2>
    <span class="intro-divider"></span>
    <p class="intro-text">Lorem ipsum dolor sit amet, consectetuer adipiscing elit, sed diam nonummy nibh euismod tincidunt ut laoreet dolore magna aliquam erat volutpat. Ut wisi enim ad minim veniam, quis nostrud exerci tation ullamcorper suscipit lobortis nisl ut aliquip ex ea commodo consequat. Duis autem vel eum iriure dolor in hendrerit in vulputate velit esse molestie consequat. <a href="#">READ MORE...</a></p>
  </section>

  <footer class="site-footer">
    <p class="footer-links"><a href="#">Terms &amp; Conditons</a><span class="sep">-</span><a href="#">Privacy Policy</a></p>
    <p class="copyright">© 2013 Wandertag, All Rights Reserved.</p>
    <ul class="social-list" aria-label="Social links">
      <li></li><li></li><li></li><li></li><li></li>
    </ul>
    <div class="footer-brand">Wandertag</div>
  </footer>
</body>
</html>
```